Powerpoint Template for a cool IT Recruiting and Consulting Company

We need to have a PowerPoint template designed for our company. We are a Technology Consulting and Recruiting company in Canada.

I'm not looking for an explosion of colours, stay elegant and sharp.

The message that it needs to portray a cool tech company utilizing the blue in our logo but also professionalism and an excitement feel about it that makes clients want to do business with us.

I have attached 2 screenshots of the logo options and also the PDF of them.

Looking forward to seeing the results.

Target Market(s)

We sell our services to Banks, Government and other Tech Companies

Industry/Entity Type

It Service

Font styles to use
Sans Serif

Colors
0592cd

Requirements
Must have
• Logo
Nice to have
• N/A
Should not have
• Lots of colours

```html
<!DOCTYPE html>
<html lang="en">
<head>
<meta charset="utf-8">
<title>Vantix Recruitment Presentation Template</title>
<link href="https://fonts.googleapis.com/css2?family=Montserrat:wght@300;400;600;700&family=Open+Sans:wght@400;600&display=swap" rel="stylesheet">
<style>
:root{
  --stage:#5e6a77;
  --navy:#2f4368;
  --navy-deep:#26375a;
  --blue:#4a6fa0;
  --sky:#6f95c2;
  --pale:#a9c3de;
  --mist:#dfe8f2;
  --ink:#3a4556;
  --grey:#8a929c;
  --line:#c9d2dc;
  --white:#ffffff;
}
*{box-sizing:border-box;margin:0;padding:0}
html,body{width:770px;height:1200px;overflow:hidden}
body{background:var(--stage);font-family:"Open Sans",Arial,sans-serif;color:var(--ink)}
.sheet{position:absolute;left:11px;top:38px;display:grid;grid-template-columns:repeat(3,244px);grid-auto-rows:153px;column-gap:8px;row-gap:8.5px}
.slide{position:relative;background:var(--white);overflow:hidden}
.abs{position:absolute}
.title{position:absolute;left:17px;top:14px;font-family:"Montserrat",Arial,sans-serif;font-size:8.5px;font-weight:400;letter-spacing:.2px;color:var(--navy);text-transform:uppercase}
.brand{position:absolute;right:6px;top:5px;display:flex;align-items:center;gap:2px;font-family:"Montserrat",Arial,sans-serif;font-weight:600;font-size:4.2px;color:var(--sky)}
.brand i{display:block;width:4px;height:4px;border-radius:50%;background:var(--sky)}
.brand.big{font-size:11px;gap:4px}
.brand.big i{width:10px;height:10px}
.foot{position:absolute;left:7px;right:7px;bottom:5px;display:flex;justify-content:space-between;font-size:2.6px;color:var(--grey)}
.t{font-size:3px;line-height:1.4;color:var(--grey)}
.tw{font-size:3px;line-height:1.4;color:#dbe4ef}
.lead{font-size:4.2px;line-height:1.35;color:var(--ink)}
.ph{position:absolute;background:linear-gradient(135deg,#7b8fa8,#3c4f70)}
.ph.light{background:linear-gradient(135deg,#e8eef6,#b9cbe0)}
.ph.cool{background:linear-gradient(160deg,#5b7da8,#1e2c4a)}
.ph.warm{background:linear-gradient(135deg,#9a8e80,#4c5870)}
.head{font-family:"Montserrat",Arial,sans-serif}
.toc{position:absolute;display:grid;grid-template-columns:1fr 1fr;column-gap:10px;row-gap:6px;left:26px;top:54px;width:200px;font-size:3px;line-height:1.35}
.toc .item{display:flex;align-items:flex-start}
.toc .num{display:flex;align-items:center;justify-content:center;width:9px;height:9px;border:0.6px solid var(--navy);font-size:3.6px;line-height:1;color:var(--navy);margin-right:4px;flex:none}
.toc .txt{display:block;font-size:3px;line-height:1.35}
.toc b{display:block;font-weight:400;font-family:"Montserrat",Arial,sans-serif;font-size:4.6px;line-height:1.2;color:var(--ink)}
.toc .t{display:block}
.bar{height:1px;background:var(--line);position:relative;margin-top:2px}
.bar span{position:absolute;left:0;top:0;height:1px;background:var(--blue)}
.avatar{width:24px;height:24px;border-radius:50%;background:linear-gradient(135deg,#cfdced,#7f97b6);margin:0 auto}
.dots{display:flex;justify-content:center;gap:1.5px;margin-top:3px}
.dots i{display:block;width:4px;height:4px;border-radius:50%;background:var(--navy)}
.tile{position:absolute;padding:4px;color:var(--white)}
.tile h4{font-family:"Montserrat",Arial,sans-serif;font-weight:400;font-size:4px;text-transform:uppercase;line-height:1.1;margin-top:13px}
</style>
</head>
<body>
<main class="sheet">

<!-- Cover light -->
<section class="slide">
  <div class="ph light" style="inset:0" role="img" aria-label="Pale blue photo of business people walking in a city"></div>
  <div class="brand big" style="right:auto;left:91px;top:33px"><i></i>Vantix</div>
  <div class="abs head" style="left:0;right:0;top:66px;text-align:center;font-weight:700;font-size:13px;color:var(--navy-deep)">THE RECRUITMENT</div>
  <div class="abs head" style="left:0;right:0;top:82px;text-align:center;font-size:5.5px;color:var(--navy)">SUBTITLE GOES HERE</div>
</section>

<!-- Cover dark -->
<section class="slide" style="background:var(--navy)">
  <div class="ph cool" style="left:100px;top:0;right:0;bottom:0;opacity:.75" role="img" aria-label="Businessman in a suit adjusting his jacket"></div>
  <div class="abs" style="inset:0;background:linear-gradient(90deg,var(--navy) 40%,rgba(47,67,104,0))"></div>
  <div class="abs head" style="left:22px;top:38px;font-weight:700;font-size:12.5px;color:var(--white)">THE RECRUITMENT</div>
  <div class="abs head" style="left:22px;top:54px;font-size:6px;color:var(--white)">SUBTITLE GOES HERE</div>
  <div class="abs tw" style="left:28px;top:110px;border-left:0.6px solid #8fa5c6;padding-left:3px;font-size:3.6px">Jan 4th, 2018<br>Author's Name<br>Vantix Corp.<br>www.vantix.example</div>
  <div class="brand big" style="right:16px;top:122px;color:var(--white)"><i style="background:var(--white)"></i>Vantix</div>
</section>

<!-- Table of content -->
<section class="slide">
  <div class="brand big" style="right:12px;top:13px"><i></i>Vantix</div>
  <div class="abs head" style="left:26px;top:27px;font-size:5px;color:var(--ink)">TABLE OF CONTENT</div>
  <div class="toc">
    <div class="item"><span class="num">1</span><span class="txt"><b>The Company</b><span class="t">Short line of intro text goes here today</span></span></div>
    <div class="item"><span class="num">5</span><span class="txt"><b>People and Technologies</b><span class="t">Short line of intro text goes here today</span></span></div>
    <div class="item"><span class="num">2</span><span class="txt"><b>Our Team</b><span class="t">Short line of intro text goes here today</span></span></div>
    <div class="item"><span class="num">6</span><span class="txt"><b>Methodology</b><span class="t">Short line of intro text goes here today</span></span></div>
    <div class="item"><span class="num">3</span><span class="txt"><b>Business Competencies</b><span class="t">Short line of intro text goes here today</span></span></div>
    <div class="item"><span class="num">7</span><span class="txt"><b>Project Case</b><span class="t">Short line of intro text goes here today</span></span></div>
    <div class="item"><span class="num">4</span><span class="txt"><b>The Advantage</b><span class="t">Short line of intro text goes here today</span></span></div>
    <div class="item"><span class="num">8</span><span class="txt"><b>Contact us</b><span class="t">Short line of intro text goes here today</span></span></div>
  </div>
</section>

<!-- The company -->
<section class="slide">
  <div class="brand"><i></i>Vantix</div>
  <div class="title">The Company</div>
  <div class="ph light" style="left:0;right:0;top:30px;height:54px;background:linear-gradient(180deg,#c9d4e2,#8896ab)" role="img" aria-label="Row of business people seated in a waiting area"></div>
  <div class="abs t" style="left:17px;top:93px;width:200px">Our team connects skilled technology people with banks, public bodies and tech firms across the country, fast and with care.</div>
  <div class="abs t" style="left:17px;top:112px;width:95px"><b style="color:var(--blue)">our mission</b> Find the right talent for every project we take on.</div>
  <div class="abs t" style="left:131px;top:112px;width:95px"><b style="color:var(--blue)">our vision</b> Be the trusted partner for teams in tech.</div>
  <div class="foot"><span>Presentation Title goes here | www.vantix.example</span><span>02</span></div>
</section>

<!-- Image style 1 -->
<section class="slide">
  <div class="brand"><i></i>Vantix</div>
  <div class="title">Image Style 1</div>
  <div class="abs" style="left:15px;top:33px;width:214px;height:96px;background:var(--navy)"></div>
  <div class="ph cool" style="left:15px;top:33px;width:125px;height:96px" role="img" aria-label="Hand touching a glowing digital chart"></div>
  <div class="abs tw" style="left:145px;top:38px;width:80px"><span style="font-size:4px;color:#fff">"A Semi Bold highlighted lines to describe the text words below can be placed here."</span><br><br>Our digital service platform gives teams one place to plan, hire and track talent across every project.<br><br>We help clients move faster with people who know the work and the market.<br><br>Not only compete, but win.</div>
  <div class="foot"><span>Presentation Title goes here | www.vantix.example</span><span>02</span></div>
</section>

<!-- Image style 2 -->
<section class="slide">
  <div class="brand"><i></i>Vantix</div>
  <div class="title">Image Style 2</div>
  <div class="abs" style="left:17px;top:38px;width:140px;height:90px;border:0.6px solid var(--sky)"></div>
  <div class="ph" style="left:130px;top:32px;width:99px;height:96px;background:linear-gradient(135deg,#d5dde6,#6a7f9c)" role="img" aria-label="Businessman holding a tablet in front of a city skyline"></div>
  <div class="abs t" style="left:23px;top:48px;width:95px"><span class="lead" style="font-size:3.8px">"A Semi Bold highlighted lines to describe the text words below can be placed here."</span><br><br>Our digital service platform gives teams one place to plan, hire and track talent.<br><br>We help clients move faster with people who know the work, and win.</div>
  <div class="foot"><span>Presentation Title goes here | www.vantix.example</span><span>02</span></div>
</section>

<!-- Image right large -->
<section class="slide">
  <div class="brand"><i></i>Vantix</div>
  <div class="title">Image Right Large</div>
  <div class="ph cool" style="left:120px;top:17px;width:118px;height:126px" role="img" aria-label="Finger pointing at a rising digital line chart"></div>
  <div class="abs t" style="left:17px;top:36px;width:92px"><span class="lead" style="font-size:3.8px">"A Semi Bold highlighted lines to describe the text words below can be placed here."</span><br><br>We match skilled people with teams that need them, from short jobs to long roles.<br><br>Each search is run by a recruiter who knows the tech and the client.<br><br>Fast answers, clear steps and people who fit from day one.</div>
  <div class="foot"><span>Presentation Title goes here | www.vantix.example</span><span>02</span></div>
</section>

<!-- Images collage -->
<section class="slide">
  <div class="brand"><i></i>Vantix</div>
  <div class="title">Images Collage</div>
  <div class="ph cool" style="left:17px;top:32px;width:101px;height:95px" role="img" aria-label="Blue screen of market numbers"></div>
  <div class="abs" style="left:121px;top:32px;width:45px;height:46px;background:var(--navy);padding:4px"><p class="tw">Short text for this image goes here.</p></div>
  <div class="ph cool" style="left:169px;top:32px;width:60px;height:46px" role="img" aria-label="Person at a glowing control screen"></div>
  <div class="ph warm" style="left:121px;top:81px;width:45px;height:46px" role="img" aria-label="City traffic at night"></div>
  <div class="abs" style="left:169px;top:81px;width:60px;height:46px;background:var(--navy);padding:4px"><p class="tw">Short text for this image can be placed here.</p></div>
  <div class="foot"><span>Presentation Title goes here | www.vantix.example</span><span>02</span></div>
</section>

<!-- Person profile -->
<section class="slide">
  <div class="brand"><i></i>Vantix</div>
  <div class="title">Person Profile</div>
  <div class="ph warm" style="left:17px;top:30px;width:78px;height:102px" role="img" aria-label="Portrait of a smiling businessman"></div>
  <div class="abs" style="left:95px;top:30px;width:45px;height:102px;background:var(--navy);padding:4px">
    <p style="font-size:4px;color:#fff">Liam Carter</p><p class="tw">Job Position</p>
    <p class="tw" style="margin-top:4px">Experience<br>• Role and years held<br>• Role and years held<br><br>Achievement<br>• Award name 2016<br>• Award name 2015</p>
  </div>
  <div class="abs" style="left:146px;top:30px;width:82px">
    <p class="lead" style="font-size:3.8px">"A Semi Bold highlighted lines to describe this person text words below can be placed here."</p>
    <p class="t" style="margin-top:3px">Short bio text for this person can go here.</p>
    <p class="t" style="margin-top:8px">Chart Sections</p><div class="bar"><span style="width:70%"></span></div>
    <p class="t" style="margin-top:6px">Chart Sections</p><div class="bar"><span style="width:60%"></span></div>
    <p class="t" style="margin-top:6px">Chart Sections</p><div class="bar"><span style="width:60%"></span></div>
  </div>
  <div class="foot"><span>Presentation Title goes here | www.vantix.example</span><span>02</span></div>
</section>

<!-- Three key point -->
<section class="slide">
  <div class="brand"><i></i>Vantix</div>
  <div class="title">Three Key Point</div>
  <div class="ph warm" style="left:17px;top:32px;width:67px;height:46px" role="img" aria-label="Team in a meeting"></div>
  <div class="ph" style="left:89px;top:32px;width:67px;height:46px;background:linear-gradient(135deg,#c9a98b,#6d7f9a)" role="img" aria-label="Hands stacked together"></div>
  <div class="ph light" style="left:161px;top:32px;width:67px;height:46px" role="img" aria-label="Colleagues talking at a desk"></div>
  <div class="abs" style="left:17px;top:78px;width:67px;height:47px;background:#505862;padding:4px;text-align:center"><p class="head" style="font-size:3.6px;color:#fff">KEY POINT 1</p><p class="tw" style="margin-top:3px">Short text for this key point fits here.</p></div>
  <div class="abs" style="left:89px;top:78px;width:67px;height:47px;background:var(--blue);padding:4px;text-align:center"><p class="head" style="font-size:3.6px;color:#fff">KEY POINT 2</p><p class="tw" style="margin-top:3px">Short text for this key point fits here.</p></div>
  <div class="abs" style="left:161px;top:78px;width:67px;height:47px;background:#6c7a8e;padding:4px;text-align:center"><p class="head" style="font-size:3.6px;color:#fff">KEY POINT 3</p><p class="tw" style="margin-top:3px">Short text for this key point fits here.</p></div>
  <div class="foot"><span>Presentation Title goes here | www.vantix.example</span><span>02</span></div>
</section>

<!-- Two images -->
<section class="slide">
  <div class="brand"><i></i>Vantix</div>
  <div class="title">Two Images</div>
  <div class="ph light" style="left:17px;top:32px;width:104px;height:74px" role="img" aria-label="Hands using a laptop with floating icons"></div>
  <div class="ph cool" style="left:124px;top:32px;width:104px;height:74px" role="img" aria-label="Glowing network over a city"></div>
  <div class="abs t" style="left:17px;top:110px;width:100px">Short caption text for this image goes here, two or three lines long in a calm tone.</div>
  <div class="abs t" style="left:124px;top:110px;width:100px">Short caption text for this image goes here, two or three lines long in a calm tone.</div>
  <div class="foot"><span>Presentation Title goes here | www.vantix.example</span><span>02</span></div>
</section>

<!-- Historical -->
<section class="slide">
  <div class="brand"><i></i>Vantix</div>
  <div class="title">Historical</div>
  <svg class="abs" style="left:0;top:0" width="244" height="153" aria-hidden="true">
    <line x1="122" y1="22" x2="122" y2="140" stroke="#c9d2dc" stroke-width="0.6"/>
    <g fill="#fff" stroke="#8a929c" stroke-width="0.6">
      <circle cx="122" cy="28" r="6"/><circle cx="122" cy="58" r="6"/><circle cx="122" cy="88" r="6"/><circle cx="122" cy="118" r="6"/>
    </g>
    <g fill="#8a929c"><circle cx="122" cy="28" r="2"/><circle cx="122" cy="58" r="2"/><circle cx="122" cy="88" r="2"/><circle cx="122" cy="118" r="2"/></g>
  </svg>
  <div class="abs t" style="left:133px;top:25px;width:85px"><b style="color:var(--ink)">2011</b><br>Your Section Title here<br><br>Short note on this year goes in these lines.</div>
  <div class="abs t" style="left:30px;top:56px;width:85px;text-align:right"><b style="color:var(--ink)">2012</b><br>Your Section Title here<br><br>Short note on this year goes in these lines.</div>
  <div class="abs t" style="left:133px;top:86px;width:85px"><b style="color:var(--ink)">2014</b><br>Your Section Title here<br><br>Short note on this year goes in these lines.</div>
  <div class="abs t" style="left:30px;top:114px;width:85px;text-align:right"><b style="color:var(--ink)">2017</b><br>Your Section Title here<br>Short note on this year.</div>
  <div class="foot"><span>Presentation Title goes here | www.vantix.example</span><span>02</span></div>
</section>

<!-- Our team -->
<section class="slide">
  <div class="brand"><i></i>Vantix</div>
  <div class="title" style="font-size:9px">Our Team</div>
  <div class="abs" style="left:14px;top:34px;width:216px;display:grid;grid-template-columns:repeat(4,1fr);gap:4px;text-align:center">
    <div><div class="avatar" role="img" aria-label="Team member portrait"></div><p style="font-size:3.8px;margin-top:3px">Nora Blake</p><p class="t">Founding Member</p><p class="t">Short bio for this person goes here.</p><div class="dots"><i></i><i></i><i></i></div></div>
    <div><div class="avatar" role="img" aria-label="Team member portrait"></div><p style="font-size:3.8px;margin-top:3px">Emma Hart</p><p class="t">Founding Member</p><p class="t">Short bio for this person goes here.</p><div class="dots"><i></i><i></i><i></i></div></div>
    <div><div class="avatar" role="img" aria-label="Team member portrait"></div><p style="font-size:3.8px;margin-top:3px">Owen Price</p><p class="t">Founding Member</p><p class="t">Short bio for this person goes here.</p><div class="dots"><i></i><i></i><i></i></div></div>
    <div><div class="avatar" role="img" aria-label="Team member portrait"></div><p style="font-size:3.8px;margin-top:3px">Ethan Cole</p><p class="t">Founding Member</p><p class="t">Short bio for this person goes here.</p><div class="dots"><i></i><i></i><i></i></div></div>
  </div>
  <div class="foot"><span>Presentation Title goes here | www.vantix.example</span><span>02</span></div>
</section>

<!-- Section divider -->
<section class="slide" style="background:var(--blue)">
  <div class="ph" style="inset:0;background:linear-gradient(135deg,#6f8fb8,#3a5580)" role="img" aria-label="Team hands stacked together, blue tinted"></div>
  <div class="abs head" style="left:34px;top:69px;display:flex;align-items:center;gap:5px;color:#fff;font-size:9px;font-weight:300"><span>01</span><span style="width:0.6px;height:14px;background:#fff"></span><span>SECTION NAME</span></div>
</section>

<!-- Methodology -->
<section class="slide">
  <div class="brand"><i></i>Vantix</div>
  <div class="title">Methodology</div>
  <div class="abs" style="left:0;top:33px;width:140px;height:96px;background:var(--navy)"></div>
  <div class="abs tw" style="left:15px;top:40px;width:50px"><span style="color:#fff">Bottle Neck</span><br>• Short point here<br>• Short point here<br>• Short point here</div>
  <div class="abs tw" style="left:74px;top:40px;width:50px"><span style="color:#fff">Action Required</span><br>• Short point here<br>• Short point here<br>• Short point here</div>
  <div class="abs tw" style="left:15px;top:73px;width:110px">This page holds the detail of your section and can be set to your needs.</div>
  <svg class="abs" style="left:15px;top:100px" width="115" height="20" aria-hidden="true">
    <line x1="0" y1="6" x2="115" y2="6" stroke="#8fa5c6" stroke-width="0.5"/>
    <g fill="none" stroke="#8fa5c6" stroke-width="0.5"><rect x="15" y="2" width="8" height="8"/><rect x="53" y="2" width="8" height="8"/><rect x="91" y="2" width="8" height="8"/></g>
  </svg>
  <div class="abs tw" style="left:22px;top:114px;width:110px;display:flex;justify-content:space-between;font-size:2.6px"><span>step one</span><span>step two</span><span>step three</span></div>
  <div class="ph light" style="left:140px;top:33px;width:104px;height:48px" role="img" aria-label="Two people talking in an office"></div>
  <div class="ph" style="left:140px;top:81px;width:104px;height:48px;background:linear-gradient(135deg,#c9a98b,#6d7f9a)" role="img" aria-label="Hands stacked together"></div>
  <div class="foot"><span>Presentation Title goes here | www.vantix.example</span><span>02</span></div>
</section>

<!-- Chart page quadrants -->
<section class="slide">
  <div class="brand"><i></i>Vantix</div>
  <div class="title">Chart Page</div>
  <svg class="abs" style="left:82px;top:40px" width="80" height="80" aria-hidden="true">
    <path d="M38 38 H4 V20 A16 16 0 0 1 20 4 H38 Z" fill="#2f4368"/>
    <path d="M42 38 V4 H60 A16 16 0 0 1 76 20 V38 Z" fill="#4a6fa0"/>
    <path d="M38 42 V76 H20 A16 16 0 0 1 4 60 V42 Z" fill="#4a6fa0"/>
    <path d="M42 42 H76 V60 A16 16 0 0 1 60 76 H42 Z" fill="#2f4368"/>
    <circle cx="40" cy="40" r="15" fill="#fff"/>
  </svg>
  <div class="abs head" style="left:107px;top:75px;width:30px;text-align:center;font-size:3px;color:var(--blue)">TARGET<br>OPPORTUNITY</div>
  <div class="abs tw" style="left:88px;top:52px;width:22px">Short label text</div>
  <div class="abs tw" style="left:136px;top:52px;width:22px;text-align:right">Short label text</div>
  <div class="abs tw" style="left:88px;top:97px;width:22px">Short label text</div>
  <div class="abs tw" style="left:136px;top:97px;width:22px;text-align:right">Short label text</div>
  <div class="abs t" style="left:17px;top:38px;width:58px"><b style="color:var(--blue)">Origination</b><br>Direct sourcing from partners<br>Size: 45 roles<br>Returns: 8% to 12%<br>Risk: low to medium<br>Regions: East and West</div>
  <div class="abs t" style="left:168px;top:38px;width:58px"><b style="color:var(--blue)">Origination</b><br>Direct sourcing from partners<br>Size: 45 roles<br>Returns: 8% to 12%<br>Risk: low to medium<br>Regions: East and West</div>
  <div class="abs t" style="left:17px;top:92px;width:58px"><b style="color:var(--blue)">Origination</b><br>Direct sourcing from partners<br>Size: 45 roles<br>Returns: 8% to 12%<br>Risk: low to medium</div>
  <div class="abs t" style="left:168px;top:92px;width:58px"><b style="color:var(--blue)">Origination</b><br>Direct sourcing from partners<br>Size: 45 roles<br>Returns: 8% to 12%<br>Risk: low to medium</div>
  <div class="foot"><span>Presentation Title goes here | www.vantix.example</span><span>02</span></div>
</section>

<!-- Our business -->
<section class="slide">
  <div class="brand"><i></i>Vantix</div>
  <div class="title">Our Business</div>
  <div class="tile" style="left:17px;top:31px;width:70px;height:46px;background:var(--pale)"><h4>Systematic<br>Trading</h4><p class="tw">Short note on this service goes here.</p></div>
  <div class="tile" style="left:89px;top:31px;width:42px;height:93px;background:var(--blue)">
    <svg width="14" height="14" style="display:block;margin-top:14px" aria-hidden="true"><g fill="none" stroke="#fff" stroke-width="0.7"><path d="M1 5 L7 1 L13 5 Z"/><line x1="3" y1="6" x2="3" y2="11"/><line x1="7" y1="6" x2="7" y2="11"/><line x1="11" y1="6" x2="11" y2="11"/><line x1="1" y1="12.5" x2="13" y2="12.5"/></g></svg>
    <h4 style="margin-top:4px">Risk<br>Management</h4><p class="tw">Short note on this service goes here in a few lines.</p></div>
  <div class="tile" style="left:133px;top:31px;width:94px;height:46px;background:var(--navy)"><h4>Historical<br>Benchmarks</h4><p class="tw">Short note on this service goes here in a couple of lines.</p></div>
  <div class="tile" style="left:17px;top:79px;width:70px;height:45px;background:var(--navy)">
    <svg width="10" height="8" class="abs" style="left:4px;top:4px" aria-hidden="true"><g fill="none" stroke="#fff" stroke-width="0.7"><path d="M1 2 H8 L6 0.5"/><path d="M9 6 H2 L4 7.5"/></g></svg>
    <h4>Direction<br>Neutral</h4><p class="tw">Short note on this service goes here.</p></div>
  <div class="tile" style="left:133px;top:79px;width:94px;height:45px;background:var(--sky)"><h4>Value Add<br>Commissions</h4><p class="tw">Short note on this service goes here in a couple of lines.</p></div>
  <div class="foot"><span>Presentation Title goes here | www.vantix.example</span><span>02</span></div>
</section>

<!-- The process -->
<section class="slide">
  <div class="brand"><i></i>Vantix</div>
  <div class="ph" style="left:0;top:0;width:56px;height:153px;background:linear-gradient(160deg,#b9c7d8,#59708f)" role="img" aria-label="Business people walking through a bright hall"></div>
  <div class="abs" style="left:56px;top:0;width:20px;height:153px;background:var(--navy)"></div>
  <div class="abs head" style="left:118px;top:13px;font-size:7.5px;color:var(--navy)">THE PROCESS</div>
  <div class="abs t" style="left:118px;top:24px;width:112px">Each search starts with a short call to learn your team, your tools and your goals. We then build a shortlist of people who fit, check skills with care and set up meetings that suit your time. Once a match is made we stay in touch to make sure the start goes well for all sides.</div>
  <div class="abs t" style="left:118px;top:78px;width:50px"><b style="color:var(--ink)">Headline 1</b><br>Short text for this step goes here.</div>
  <div class="abs t" style="left:178px;top:78px;width:50px"><b style="color:var(--ink)">Headline 2</b><br>Short text for this step goes here.</div>
  <div class="abs t" style="left:118px;top:102px;width:50px"><b style="color:var(--ink)">Headline 3</b><br>Short text for this step goes here.</div>
  <div class="abs t" style="left:178px;top:102px;width:50px"><b style="color:var(--ink)">Headline 4</b><br>Short text for this step goes here.</div>
  <div class="foot" style="left:82px"><span>Presentation Title goes here | www.vantix.example</span><span>02</span></div>
</section>

<!-- Chart page donut -->
<section class="slide">
  <div class="brand"><i></i>Vantix</div>
  <div class="title">Chart Page</div>
  <div class="abs t" style="left:0;right:0;top:24px;text-align:center;font-size:3.6px;color:var(--ink)">Put your highlight here as main statement of the diagram</div>
  <svg class="abs" style="left:92px;top:48px" width="60" height="60" viewBox="0 0 60 60" aria-hidden="true">
    <g fill="none" stroke-width="11" transform="rotate(-90 30 30)">
      <circle cx="30" cy="30" r="22" stroke="#4a6fa0" stroke-dasharray="21 117.2" stroke-dashoffset="0"/>
      <circle cx="30" cy="30" r="22" stroke="#6f95c2" stroke-dasharray="21 117.2" stroke-dashoffset="-23"/>
      <circle cx="30" cy="30" r="22" stroke="#5aa0a8" stroke-dasharray="21 117.2" stroke-dashoffset="-46"/>
      <circle cx="30" cy="30" r="22" stroke="#8cb86a" stroke-dasharray="21 117.2" stroke-dashoffset="-69"/>
      <circle cx="30" cy="30" r="22" stroke="#2f4368" stroke-dasharray="21 117.2" stroke-dashoffset="-92"/>
      <circle cx="30" cy="30" r="22" stroke="#c9b37c" stroke-dasharray="21 117.2" stroke-dashoffset="-115"/>
    </g>
  </svg>
  <div class="abs t" style="left:22px;top:44px;width:60px;text-align:right">Short note for this part of the chart goes here.</div>
  <div class="abs t" style="left:22px;top:74px;width:60px;text-align:right">Short note for this part of the chart goes here.</div>
  <div class="abs t" style="left:22px;top:104px;width:60px;text-align:right">Short note for this part of the chart goes here.</div>
  <div class="abs t" style="left:162px;top:44px;width:60px">Short note for this part of the chart goes here.</div>
  <div class="abs t" style="left:162px;top:74px;width:60px">Short note for this part of the chart goes here.</div>
  <div class="abs t" style="left:162px;top:104px;width:60px">Short note for this part of the chart goes here.</div>
  <div class="foot"><span>Presentation Title goes here | www.vantix.example</span><span>02</span></div>
</section>

<!-- Testimonial -->
<section class="slide">
  <div class="brand"><i></i>Vantix</div>
  <div class="title">Testimonial</div>
  <div class="ph warm" style="left:42px;top:45px;width:52px;height:62px" role="img" aria-label="Portrait of a smiling client"></div>
  <div class="abs" style="left:101px;top:45px;width:107px;height:62px;border:0.6px solid var(--sky);padding:6px 8px">
    <span class="abs head" style="left:2px;top:0;font-size:7px;line-height:1;color:var(--navy)">“</span>
    <p class="t">The team found us three strong people in two weeks and kept in touch the whole way through. Clear, fast and easy to work with.<br><br>We now call them first for every new role we open.</p>
    <span class="abs head" style="right:3px;bottom:0;font-size:7px;line-height:1;color:var(--navy)">”</span>
  </div>
  <div class="foot"><span>Presentation Title goes here | www.vantix.example</span><span>02</span></div>
</section>

<!-- Thank you -->
<section class="slide">
  <div class="brand big" style="right:14px;top:14px"><i></i>Vantix</div>
  <div class="abs head" style="left:22px;top:39px;font-size:8.5px;color:var(--navy)">THANK YOU.</div>
  <div class="abs" style="left:0;right:0;top:90px;bottom:0;background:var(--navy)"></div>
  <svg class="abs" style="left:22px;top:85px" width="150" height="12" aria-hidden="true">
    <g fill="#fff" stroke="#2f4368" stroke-width="0.6"><rect x="0" y="1" width="10" height="10"/><rect x="60" y="1" width="10" height="10"/><rect x="122" y="1" width="10" height="10"/></g>
    <g fill="none" stroke="#2f4368" stroke-width="0.6">
      <rect x="2.5" y="4" width="5" height="4"/><path d="M2.5 4 L5 6 L7.5 4"/>
      <path d="M63 3.5 Q63 8.5 67.5 9 L67.5 7.5 L66 7 L65 7.8 Q63.8 6.5 64 5 L64.8 4.8 L64.5 3.2 Z"/>
      <circle cx="127" cy="5" r="1.6"/><path d="M127 9.5 L125 6 M127 9.5 L129 6"/>
    </g>
  </svg>
  <div class="abs tw" style="left:22px;top:103px;font-size:3.4px">Vantix Corp.<br>120 Harbour Lane, Region.</div>
  <div class="abs tw" style="left:82px;top:103px;font-size:3.4px">T 555 010 246<br>F 555 010 642</div>
  <div class="abs tw" style="left:144px;top:103px;font-size:3.4px">info@vantix.example<br>www.vantix.example</div>
  <div class="abs" style="left:22px;top:126px;display:flex;gap:1.5px;align-items:center;font-size:3px;line-height:1"><i style="width:5px;height:5px;background:#fff;display:block"></i><i style="width:5px;height:5px;background:#fff;display:block"></i><i style="width:5px;height:5px;background:#fff;display:block"></i><span class="tw" style="margin-left:2px">Vantix</span></div>
</section>

</main>
</body>
</html>
```